Flyer for Corvane Visual - Design Agency

We need a 4-page square flyer measuring 14.8x14.8cm per page, to fold out, for a design agency targeting small businesses.
The design should be very modern. There shouldn't be too much content visible.
The background should be black. The color of the logo (attached) can also be used. The content is also attached and divided per page. We are open to alternative suggestions regarding the division.

```html
<!DOCTYPE html>
<html lang="de">
<head>
<meta charset="utf-8">
<title>Corvane Visual – Flyer</title>
<link href="https://fonts.googleapis.com/css2?family=Poppins:wght@400;500;600;700&display=swap" rel="stylesheet">
<style>
:root{
  --page:#ffffff;
  --black:#000000;
  --ink:#050a0b;
  --teal:#5ff3e4;
  --teal-strong:#1fe0cf;
  --teal-deep:#0b3b3b;
  --white:#ffffff;
  --muted:#cfd8d8;
}
*{margin:0;padding:0;box-sizing:border-box}
html,body{width:1200px;height:2278px;overflow:hidden;background:var(--page);font-family:"Poppins",sans-serif}
.spread{position:absolute;left:40px;width:1120px;height:564px;background:var(--black);overflow:hidden;color:var(--white)}
.spread--outer{top:545px}
.spread--inner{top:1169px}
.abs{position:absolute}
.brand{font-weight:600;color:var(--teal);line-height:1;letter-spacing:-0.5px}

/* outer spread */
.glow-backdrop{left:0;top:0;width:560px;height:564px;background:radial-gradient(ellipse 60% 55% at 50% 28%,#0e3f3c 0%,#06201f 45%,#000 80%)}
.outer-logo{left:0;width:560px;top:238px;text-align:center;font-size:34px}
.claim{left:0;width:560px;top:312px;text-align:center;font-size:21px;font-weight:600;line-height:25px}
.claim span{color:var(--teal)}
.cta{left:68px;top:372px;width:392px;height:24px;border-radius:12px;background:var(--teal);color:var(--black);font-size:14.5px;font-weight:500;text-align:center;line-height:24px}
.contact{font-size:13.5px;font-weight:500;display:flex;gap:8px;align-items:flex-start;line-height:16px}
.contact .ico{width:18px;height:18px;border-radius:50%;background:var(--teal);flex:none;display:flex;align-items:center;justify-content:center}
.owner{left:114px;top:484px;display:flex;align-items:center;gap:10px;font-size:14px;letter-spacing:2px}
.owner .tag{background:var(--teal);color:var(--black);font-weight:600;font-size:13px;letter-spacing:0;border-radius:10px;padding:0 13px;line-height:20px}
.cover-logo{left:630px;top:82px;font-size:38px}
.cover-head{left:631px;top:218px;font-weight:600;font-size:28px;line-height:31px}
.cover-head .big{color:var(--teal);font-size:43px;line-height:46px;font-weight:700}
.cover-head .gap{margin-top:8px}
.collage{left:850px;top:72px;width:230px;height:404px}
.url{font-size:18px;letter-spacing:0.5px}
.url b{color:var(--teal);font-weight:600}
.cover-url{left:633px;top:494px}

/* inner spread */
.inner-right-bg{left:560px;top:0;width:560px;height:564px;background:linear-gradient(160deg,#020606 0%,#0a2e2e 55%,#0d3a3a 100%)}
.tagline{left:77px;top:56px;color:var(--teal);font-size:26px;font-weight:600}
.mini-logo{left:78px;top:104px;font-size:26px}
.tagline-sub{left:197px;top:102px;font-size:21px;font-weight:600;line-height:26px}
.bulb{left:40px;top:178px;width:230px;height:386px}
.promise{left:293px;top:213px;width:207px;height:228px;border:2px solid var(--teal);border-radius:20px;padding:26px 20px 0 34px;font-size:15.5px;font-weight:500;line-height:19px}
.promise .plus{display:block;margin-top:16px;color:var(--teal);font-size:23px;font-weight:600}
.services{left:623px;top:58px;width:235px;height:380px;border-radius:18px 18px 0 0;background:linear-gradient(180deg,var(--teal-strong) 0%,#17bdb0 40%,#109488 62%,#0a4a46 85%,rgba(10,40,40,0) 100%);padding:20px 18px 0 24px}
.services h2{font-size:15px;font-weight:600;color:var(--ink);margin-bottom:16px}
.service{display:flex;gap:9px;margin-bottom:11px}
.service .dot{width:22px;height:22px;border-radius:50%;background:#0d2a2a;flex:none;margin-top:1px;border:2px solid #2a4b4b}
.service h3{font-size:12.5px;font-weight:600;color:#082020;line-height:15px}
.service p{font-size:9.5px;line-height:11.5px;color:#0b2d2d}
.why{left:880px;top:58px;width:210px}
.why h2{font-size:15px;font-weight:600;color:var(--teal);margin-bottom:14px}
.why-item{margin-bottom:13px;padding-left:16px;position:relative}
.why-item::before{content:"";position:absolute;left:2px;top:5px;width:7px;height:7px;border-radius:50%;border:2px solid var(--teal)}
.why-item h3{font-size:12.5px;font-weight:600;line-height:15px}
.why-item p{font-size:9.5px;line-height:11.5px;color:var(--muted);max-width:150px}
.workspace{left:905px;top:248px;width:190px;height:160px;border-radius:6px}
.inner-logo{left:622px;top:470px;font-size:32px}
.inner-url{left:880px;top:482px}
</style>
</head>
<body>

<section class="spread spread--outer">
  <div class="abs glow-backdrop" role="img" aria-label="Dunkler Hintergrund mit leuchtenden türkisen Neon-Dreiecken"></div>
  <div class="abs brand outer-logo">Corvane Visual</div>
  <p class="abs claim">Designs, die wirken Marken,<br><span>die bleiben.</span></p>
  <div class="abs cta">Kontaktiere uns für eine kostenlose Beratung!</div>

  <div class="abs contact" style="left:65px;top:413px">
    <span class="ico"><svg width="10" height="10" viewBox="0 0 24 24"><path fill="#000" d="M6.6 10.8a15 15 0 0 0 6.6 6.6l2.2-2.2c.3-.3.7-.4 1-.2 1.1.4 2.3.6 3.6.6.6 0 1 .4 1 1V20c0 .6-.4 1-1 1A17 17 0 0 1 3 4c0-.6.4-1 1-1h3.5c.6 0 1 .4 1 1 0 1.3.2 2.5.6 3.6.1.3 0 .7-.2 1z"/></svg></span>
    <span>+49 123 98210</span>
  </div>
  <div class="abs contact" style="left:65px;top:440px">
    <span class="ico"><svg width="11" height="11" viewBox="0 0 24 24" fill="none" stroke="#000" stroke-width="2"><circle cx="12" cy="12" r="9"/><path d="M3 12h18M12 3c3 3 3 15 0 18M12 3c-3 3-3 15 0 18"/></svg></span>
    <span>www.corvanevisual.de</span>
  </div>
  <div class="abs contact" style="left:277px;top:413px">
    <span class="ico"><svg width="10" height="10" viewBox="0 0 24 24" fill="none" stroke="#000" stroke-width="2.4"><rect x="3" y="5" width="18" height="14" rx="1"/><path d="M3 6l9 7 9-7"/></svg></span>
    <span>design@corvanevisual.de</span>
  </div>
  <div class="abs contact" style="left:277px;top:440px">
    <span class="ico"><svg width="10" height="11" viewBox="0 0 24 24"><path fill="#000" d="M12 2a7 7 0 0 0-7 7c0 5 7 13 7 13s7-8 7-13a7 7 0 0 0-7-7zm0 9.5A2.5 2.5 0 1 1 12 6.5a2.5 2.5 0 0 1 0 5z"/></svg></span>
    <span>Lindenweg 42<br>60311 Frankfurt</span>
  </div>
  <div class="abs owner"><span class="tag">Inhaber</span><span>Lena Roth &amp; Tomas Weber</span></div>

  <div class="abs brand cover-logo">Corvane Visual</div>
  <div class="abs cover-head">
    Dein<br>Unternehmen.<br><div class="gap">Dein Stil.</div>
    <div class="big">Unser<br>Design.</div>
  </div>
  <div class="abs collage" role="img" aria-label="Halbkreis-Collage mit Ideen-Glühbirne, Arbeitsplatz in Türkis und Laptop mit Design-Skizze, mittig ein Zeichenfeder-Symbol"
       style="background:linear-gradient(180deg,#f2f2f2 0%,#e8e8e8 32%,#1b8f86 38%,#2ec9b8 62%,#d9c7ad 70%,#e9ddc9 100%);border-radius:200px 0 0 200px / 202px 0 0 202px;border-right:30px solid var(--teal)"></div>
  <div class="abs url cover-url">www.<b>corvanevisual</b>.de</div>
</section>

<section class="spread spread--inner">
  <div class="abs inner-right-bg"></div>
  <h1 class="abs tagline">Modern, mutig, markant</h1>
  <div class="abs brand mini-logo">Corvane</div>
  <p class="abs tagline-sub">gestaltet die Zukunft deines<br>Unternehmensauftritts.</p>
  <div class="abs bulb" role="img" aria-label="Leuchtende Neon-Glühbirne in Türkis mit dem Schriftzug Idea auf dunklem Grund"
       style="background:radial-gradient(ellipse at 45% 45%,#1fe0cf 0%,#0c6f6a 30%,#061a1c 60%,#000 75%);border-radius:40% 40% 8px 8px"></div>
  <div class="abs promise">Wir machen aus Ideen visuelle Erlebnisse und sorgen dafür, dass deine Marke im Gedächtnis bleibt.<span class="plus">+ Grafiken</span></div>

  <div class="abs services">
    <h2>Unsere Leistungen</h2>
    <div class="service"><span class="dot"></span><div><h3>Next-Level Flyer</h3><p>Nicht nur Papier, sondern deine Botschaft im perfekten Look.</p></div></div>
    <div class="service"><span class="dot"></span><div><h3>Corporate Identity</h3><p>Ein Design, das deine Marke spricht – individuell, stark, unvergesslich.</p></div></div>
    <div class="service"><span class="dot"></span><div><h3>Digital &amp; Print</h3><p>Ob Social Media Grafiken oder klassisches Printdesign – wir sind da, wo du uns brauchst.</p></div></div>
    <div class="service"><span class="dot"></span><div><h3>Alles aus einer Hand</h3><p>Logo, Farben, Typografie, Flyer und vieles mehr – wir bauen das Fundament für deinen Erfolg.</p></div></div>
  </div>

  <div class="abs why">
    <h2>Warum wir?</h2>
    <div class="why-item"><h3>Dein Style, unser Know-how</h3><p>Wir kombinieren deine Vision mit moderner Ästhetik.</p></div>
    <div class="why-item"><h3>Persönlicher Service</h3><p>Wir hören zu und setzen um, was dich einzigartig macht.</p></div>
    <div class="why-item"><h3>Flexible Lösungen</h3><p>für die unterschiedlichsten Anforderungen</p></div>
  </div>
  <div class="abs workspace" role="img" aria-label="Laptop mit Zeichenfeder, Farbfächer und Kaffeetasse"
       style="background:linear-gradient(160deg,#e0a43a 0%,#9aa0a6 35%,#c0c4c8 70%,#e8e8e8 100%);opacity:.85"></div>

  <div class="abs brand inner-logo">Corvane Visual</div>
  <div class="abs url inner-url">www.<b>corvanevisual</b>.de</div>
</section>

</body>
</html>
```